Business Card design for construction company

I would like a business card design for a construction company - Harlow Constructions. I have attached the ai logo file for use. I would like the card to be very smart and clean and incorporate only white and the two colours in the logo. I would like the card to have two sides. One side can just have the logo, the other with the relevant information.

Target Market(s)

Building and Construction Clients

Industry/Entity Type

Business

Contact Information for Business Card

Name: Tom Pardoe
Company: Harlow Constructions Pty Limited
Address: 14 Mallee Crescent Carrow Vale 2093
Phone: 0427 531 068
Email: tomp@harlowbuild-example.com.au

Font styles to use
Serif
Sans Serif

Requirements
Must have
• Details noted above
• Logo as provided
• Colours as in logo
• Square edges
• A font that compliments the logo
Should not have
• Any colour other than white and those in logo
• Rounded edges

```html
<!DOCTYPE html>
<html lang="en">
<head>
<meta charset="utf-8">
<title>Harlow Constructions – Business Card</title>
<link href="https://fonts.googleapis.com/css2?family=Arimo:wght@400;700&display=swap" rel="stylesheet">
<style>
  :root {
    --brand-blue: #1ba9e6;
    --brand-grey: #58585a;
    --paper: #ffffff;
    --backdrop: #8a8a8c;
    --text-grey: #4a4a4c;
  }
  * { margin: 0; padding: 0; box-sizing: border-box; }
  html, body { width: 1200px; height: 1200px; overflow: hidden; }
  body {
    background: radial-gradient(circle at 50% 45%, #c9c9ca 0%, var(--backdrop) 75%);
    font-family: "Arimo", Arial, sans-serif;
    display: flex; flex-direction: column; align-items: center; justify-content: center;
    gap: 80px;
  }
  .card {
    position: relative;
    width: 800px; height: 476px;
    box-shadow: 0 10px 24px rgba(0,0,0,.35);
    overflow: hidden;
  }
  .card--front { background: var(--paper); }
  .card--back { background: var(--brand-grey); }

  .wordmark {
    position: absolute;
    font-size: 26px; font-weight: 400; letter-spacing: 4px;
    text-transform: uppercase; white-space: nowrap;
  }
  .card--front .wordmark { top: 60px; right: 46px; color: var(--brand-grey); }
  .card--back .wordmark { top: 208px; left: 0; right: 0; text-align: center; color: var(--paper); font-size: 30px; }

  .holder { position: absolute; left: 48px; top: 238px; }
  .holder__name { color: var(--brand-blue); font-weight: 700; font-size: 40px; letter-spacing: -.5px; }
  .holder__title { color: var(--text-grey); font-size: 18px; margin-top: 6px; letter-spacing: .3px; }

  .rule { position: absolute; top: 324px; height: 6px; }
  .rule--blue { left: 48px; width: 208px; background: var(--brand-blue); }
  .rule--grey { left: 264px; width: 490px; background: var(--brand-grey); }

  .contact { position: absolute; color: var(--text-grey); font-size: 21px; line-height: 32px; }
  .contact--left { left: 46px; top: 354px; }
  .contact--right { left: 468px; top: 354px; }
  .contact__row { display: flex; align-items: center; gap: 12px; }
  .contact__icon { width: 28px; height: 28px; flex: none; }
  .contact__address { padding-left: 40px; }

  .footer-band { position: absolute; left: 0; right: 0; bottom: 0; height: 46px; background: var(--brand-grey); display: flex; }
  .footer-band__home { width: 88px; height: 100%; background: var(--brand-blue); display: flex; align-items: center; justify-content: center; margin-right: 6px; border-right: 6px solid var(--paper); }
  .footer-band__web { color: var(--paper); font-size: 22px; line-height: 46px; padding-left: 14px; }

  .legal-name {
    position: absolute; left: 0; right: 0; bottom: 36px; text-align: center;
    color: var(--paper); font-weight: 700; font-size: 22px; letter-spacing: -.2px;
  }
</style>
</head>
<body>

<section class="card card--front">
  <div class="wordmark">Harlow Constructions</div>

  <div class="holder">
    <div class="holder__name">Tom Pardoe</div>
    <div class="holder__title">MANAGING DIRECTOR</div>
  </div>

  <div class="rule rule--blue"></div>
  <div class="rule rule--grey"></div>

  <div class="contact contact--left">
    <div class="contact__row">
      <svg class="contact__icon" viewBox="0 0 28 28" aria-hidden="true">
        <circle cx="14" cy="14" r="12" fill="none" stroke="var(--brand-grey)" stroke-width="2.2"/>
        <path d="M10 8.5c-1 .6-1.6 1.6-1 3.2 1.2 3.2 3.7 5.9 6.9 7.3 1.5.6 2.6 0 3.2-1l-2.3-2.2-1.6.9c-1.6-.8-2.9-2.2-3.6-3.8l1-1.5z" fill="var(--brand-blue)"/>
      </svg>
      <span>0427 531 068</span>
    </div>
    <div class="contact__row">
      <svg class="contact__icon" viewBox="0 0 28 28" aria-hidden="true">
        <circle cx="14" cy="14" r="12" fill="none" stroke="var(--brand-grey)" stroke-width="2.2"/>
        <rect x="8" y="10" width="12" height="9" fill="var(--brand-blue)"/>
        <path d="M8 10l6 5 6-5" fill="none" stroke="var(--paper)" stroke-width="1.4"/>
      </svg>
      <span>tomp@harlowbuild-example.com.au</span>
    </div>
  </div>

  <div class="contact contact--right">
    <div class="contact__row">
      <svg class="contact__icon" viewBox="0 0 28 28" aria-hidden="true">
        <circle cx="14" cy="14" r="12" fill="none" stroke="var(--brand-grey)" stroke-width="2.2"/>
        <path d="M14 6.5a5 5 0 0 0-5 5c0 3.6 5 9.5 5 9.5s5-5.9 5-9.5a5 5 0 0 0-5-5z" fill="var(--brand-blue)"/>
        <circle cx="14" cy="11.5" r="1.9" fill="var(--paper)"/>
      </svg>
      <span>14 Mallee Crescent</span>
    </div>
    <div class="contact__address">Carrow Vale 2093</div>
  </div>

  <div class="footer-band">
    <div class="footer-band__home">
      <svg width="24" height="22" viewBox="0 0 24 22" aria-hidden="true">
        <path d="M12 1L1 11h3v10h6v-6h4v6h6V11h3z" fill="var(--paper)"/>
      </svg>
    </div>
    <div class="footer-band__web">www.harlowbuild-example.com.au</div>
  </div>
</section>

<section class="card card--back">
  <div class="wordmark">Harlow Constructions</div>
  <div class="legal-name">HARLOW CONSTRUCTIONS PTY LIMITED</div>
</section>

</body>
</html>
```